Brimovex business card

Based on company logo and website given , to design a business card temple. Slogan "Your furry friends deserves the best"
Color style please refer to our website

```html
<!DOCTYPE html>
<html lang="en">
<head>
<meta charset="utf-8">
<title>Brimovex business card</title>
<link rel="stylesheet" href="https://fonts.googleapis.com/css2?family=Montserrat:wght@700;800&family=Questrial&display=swap">
<style>
  :root {
    --backdrop: #e4e0d8;
    --blue-light: #3b82d0;
    --blue-mid: #1f5fbf;
    --blue-deep: #0f3a9c;
    --paper: #f7f7f7;
    --ink-grey: #707070;
    --white: #ffffff;
    --divider: rgba(255, 255, 255, 0.45);
  }
  * { box-sizing: border-box; margin: 0; padding: 0; }
  html, body {
    width: 1200px;
    height: 800px;
    overflow: hidden;
  }
  body {
    background: var(--backdrop);
    display: flex;
    align-items: center;
    justify-content: center;
    gap: 40px;
    font-family: "Questrial", sans-serif;
  }
  .card {
    width: 520px;
    height: 297px;
    position: relative;
    overflow: hidden;
    box-shadow: 0 18px 30px rgba(60, 50, 40, 0.22);
  }

  /* Front side */
  .card-front {
    background: linear-gradient(135deg, var(--blue-light) 0%, var(--blue-mid) 60%, var(--blue-deep) 100%);
    display: flex;
    flex-direction: column;
    align-items: center;
    justify-content: center;
    color: var(--white);
  }
  .brand {
    display: flex;
    align-items: center;
    gap: 10px;
    font-family: "Questrial", sans-serif;
    font-size: 46px;
    line-height: 1;
    letter-spacing: 0.5px;
  }
  .brand-dot {
    width: 14px;
    height: 14px;
    border-radius: 50%;
    background: currentColor;
  }
  .slogan {
    margin-top: 16px;
    font-size: 16px;
    letter-spacing: 0.3px;
  }

  /* Back side */
  .card-back {
    background: var(--paper);
  }
  .identity {
    position: absolute;
    left: 34px;
    top: 30px;
  }
  .person-name {
    font-family: "Montserrat", sans-serif;
    font-weight: 800;
    font-size: 30px;
    color: var(--blue-mid);
    line-height: 1.05;
  }
  .person-role {
    font-size: 17px;
    color: var(--ink-grey);
    margin-top: 2px;
  }
  .identity-rule {
    width: 28px;
    height: 3px;
    background: var(--blue-mid);
    margin-top: 8px;
  }
  .card-back .brand {
    position: absolute;
    right: 30px;
    top: 78px;
    font-size: 32px;
    color: var(--blue-deep);
    gap: 7px;
  }
  .card-back .brand-dot { width: 10px; height: 10px; }
  .contact-band {
    position: absolute;
    left: 0;
    right: 0;
    bottom: 0;
    height: 150px;
    background: linear-gradient(90deg, var(--blue-mid) 0%, var(--blue-deep) 100%);
    display: flex;
    align-items: center;
    padding: 0 16px;
    color: var(--white);
  }
  .contact-item {
    flex: 1;
    display: flex;
    flex-direction: column;
    align-items: center;
    text-align: center;
    font-size: 13px;
    line-height: 1.4;
  }
  .contact-item + .contact-item {
    border-left: 1px solid var(--divider);
  }
  .contact-icon {
    width: 20px;
    height: 20px;
    margin-bottom: 12px;
  }
</style>
</head>
<body>

  <section class="card card-front" aria-label="Card front">
    <div class="brand"><span class="brand-dot"></span><span>Brimovex</span></div>
    <p class="slogan">Your furry friends deserves the best</p>
  </section>

  <section class="card card-back" aria-label="Card back">
    <div class="identity">
      <h1 class="person-name">Owen Harlow</h1>
      <p class="person-role">Manager</p>
      <div class="identity-rule"></div>
    </div>

    <div class="brand"><span class="brand-dot"></span><span>Brimovex</span></div>

    <div class="contact-band">
      <div class="contact-item contact-phone">
        <svg class="contact-icon" viewBox="0 0 24 24" aria-hidden="true">
          <path fill="#fff" d="M6.6 10.8a15.2 15.2 0 0 0 6.6 6.6l2.2-2.2a1 1 0 0 1 1-.25 11.4 11.4 0 0 0 3.6.57 1 1 0 0 1 1 1V20a1 1 0 0 1-1 1A17 17 0 0 1 3 4a1 1 0 0 1 1-1h3.5a1 1 0 0 1 1 1c0 1.25.2 2.45.57 3.57a1 1 0 0 1-.25 1z"/>
        </svg>
        <span>1800 555 014</span>
        <span>1800 555 014</span>
      </div>
      <div class="contact-item contact-web">
        <svg class="contact-icon" viewBox="0 0 24 24" aria-hidden="true" fill="none" stroke="#fff" stroke-width="1.8">
          <circle cx="12" cy="12" r="9.5"/>
          <ellipse cx="12" cy="12" rx="4.2" ry="9.5"/>
          <line x1="2.5" y1="12" x2="21.5" y2="12"/>
          <path d="M4.2 7h15.6M4.2 17h15.6"/>
        </svg>
        <span>www.brimovex.com.au</span>
        <span>sales@brimovex.com.au</span>
      </div>
      <div class="contact-item contact-address">
        <svg class="contact-icon" viewBox="0 0 24 24" aria-hidden="true">
          <path fill="#fff" d="M12 2a7 7 0 0 0-7 7c0 5.2 7 13 7 13s7-7.8 7-13a7 7 0 0 0-7-7zm0 9.5A2.5 2.5 0 1 1 12 6.5a2.5 2.5 0 0 1 0 5z"/>
        </svg>
        <span>4/22 Calder Street Glen</span>
        <span>Iris Vic 3146</span>
      </div>
    </div>
  </section>

</body>
</html>
```